8X8 Realtor Training Expo Flyer

BRAVO SUMMIT REALTY & HALCYON REALTY VENTURES
INVITE ALL TO OUR
LIVE REALTOR TRAINING EXPO

WITH TRAINER / SPEAKER MR. GORDON ALAPATI
SATURDAY AUGUST 13th
9 AM - 1 PM
AT THE MARWICK LODGE
4817 HOLLOWAY CREEK DRIVE
GREENBELT, MD 20770

RSVP PREFERRED BY EMAILING FRONTDESK@BRAVOSUMMITREALTY.COM

```html
<!DOCTYPE html>
<html lang="en">
<head>
<meta charset="utf-8">
<title>Live Realtor Training Expo</title>
<link rel="stylesheet" href="https://fonts.googleapis.com/css2?family=Jost:wght@500;600;700&family=Yellowtail&display=swap">
<style>
  :root {
    --teal: #0f8f9c;
    --teal-light: #22a3ae;
    --ink: #0b0b0b;
    --paper: #ffffff;
    --paper-shade: #ececec;
    --crowd-dark: #4a3f3a;
    --crowd-mid: #8f7f78;
    --crowd-light: #c9beb6;
    --portrait-wall: #e8d6a8;
    --portrait-suit: #2a1f1a;
  }
  * { margin: 0; padding: 0; box-sizing: border-box; }
  html, body { width: 1200px; height: 1200px; overflow: hidden; background: var(--paper); }
  .flyer { position: relative; width: 1200px; height: 1200px; overflow: hidden; font-family: 'Jost', sans-serif; }
  .backdrop { position: absolute; inset: 0; }
  .text { position: absolute; white-space: nowrap; }
  .invite-script { left: 300px; width: 846px; top: 44px; text-align: right; font-family: 'Yellowtail', cursive; font-size: 128px; line-height: 1; color: var(--ink); overflow: hidden; }
  .event-title { left: 170px; width: 980px; top: 178px; text-align: right; font-size: 63px; line-height: 1.1; font-weight: 600; color: var(--teal); }
  .event-when { left: 300px; width: 822px; top: 262px; text-align: right; font-size: 40px; line-height: 1.1; font-weight: 600; color: var(--ink); }
  .speaker-role { left: 612px; top: 378px; font-size: 39px; line-height: 1.1; font-weight: 600; color: var(--paper); }
  .speaker-name { left: 612px; top: 428px; font-size: 46px; line-height: 1.1; font-weight: 700; color: var(--paper); }
  .rsvp { left: 0; right: 0; top: 983px; text-align: center; font-size: 31px; line-height: 1.1; font-weight: 600; color: var(--paper); }
  .venue { left: 67px; top: 1052px; font-size: 37px; font-weight: 500; line-height: 43px; color: var(--ink); font-style: normal; }
  .brokerages { position: absolute; left: 690px; top: 1086px; display: flex; gap: 36px; }
  .brokerage { display: flex; align-items: center; gap: 10px; font-size: 18px; font-weight: 700; line-height: 22px; color: var(--teal); }
  .brokerage-mark { width: 22px; height: 22px; background: var(--teal); flex: none; }
</style>
</head>
<body>
<main class="flyer">
  <svg class="backdrop" width="1200" height="1200" viewBox="0 0 1200 1200">
    <defs>
      <linearGradient id="crowdTone" x1="0" y1="0" x2="0" y2="1">
        <stop offset="0" stop-color="var(--crowd-light)"/>
        <stop offset="0.45" stop-color="var(--crowd-mid)"/>
        <stop offset="1" stop-color="var(--crowd-dark)"/>
      </linearGradient>
      <linearGradient id="portraitTone" x1="0" y1="0" x2="0" y2="1">
        <stop offset="0" stop-color="var(--portrait-wall)"/>
        <stop offset="0.45" stop-color="#b8956a"/>
        <stop offset="0.7" stop-color="var(--portrait-suit)"/>
        <stop offset="1" stop-color="var(--portrait-suit)"/>
      </linearGradient>
      <linearGradient id="sheen" x1="0" y1="0" x2="1" y2="1">
        <stop offset="0" stop-color="var(--paper)"/>
        <stop offset="0.6" stop-color="var(--paper)"/>
        <stop offset="1" stop-color="var(--paper-shade)"/>
      </linearGradient>
    </defs>
    <rect class="paper" width="1200" height="1200" fill="url(#sheen)"/>
    <rect class="audience-photo" x="0" y="470" width="1200" height="500" fill="url(#crowdTone)" role="img" aria-label="Photo of a seated audience at a training seminar"/>
    <path class="side-wedge" d="M0 0 H58 C52 170 78 280 130 345 C170 395 200 420 240 440 L0 600 Z" fill="var(--teal)"/>
    <path class="side-stripe" d="M38 0 H84 C78 160 100 260 150 330 L128 345 C78 280 50 170 38 0 Z" fill="var(--ink)"/>
    <path class="swoosh-band" d="M260 430 C560 395 900 385 1200 388 V605 C1000 545 720 490 420 500 C330 505 280 520 200 540 Z" fill="var(--teal)" opacity="0.95"/>
    <path class="swoosh-glow" d="M420 500 C720 490 1000 545 1200 605 V725 C1000 640 720 560 420 520 Z" fill="var(--teal-light)" opacity="0.55"/>
    <path class="swoosh-stripe" d="M300 430 C600 380 900 362 1200 372 V402 C900 390 600 400 300 440 Z" fill="var(--ink)"/>
    <rect class="rsvp-band" x="0" y="966" width="1200" height="70" fill="var(--teal)"/>
    <circle class="portrait-frame" cx="211" cy="479" r="178" fill="var(--paper)"/>
    <circle class="portrait" cx="211" cy="479" r="168" fill="url(#portraitTone)" role="img" aria-label="Portrait of the trainer and speaker in a dark suit"/>
  </svg>

  <div class="text invite-script">Invite all to our</div>
  <h1 class="text event-title">LIVE REALTOR TRAINING EXPO</h1>
  <p class="text event-when">SATURDAY AUGUST 13th | 9 AM - 1 PM</p>
  <p class="text speaker-role">WITH TRAINER /SPEAKER</p>
  <p class="text speaker-name">MR. GORDON ALAPATI</p>
  <p class="text rsvp">RSVP PREFERRED BY EMAILING FRONTDESK@BRAVOSUMMITREALTY.COM</p>
  <address class="text venue">AT THE MARWICK LODGE<br>4817 HOLLOWAY CREEK DRIVE<br>GREENBELT, MD 20770</address>
  <div class="brokerages">
    <div class="brokerage"><span class="brokerage-mark"></span><span>BRAVO SUMMIT<br>REALTY GROUP</span></div>
    <div class="brokerage"><span class="brokerage-mark"></span><span>HALCYON REALTY<br>VENTURES</span></div>
  </div>
</main>
</body>
</html>
```